Medical Prescription for Diagnostic Sleep Testing

Quiet Harbor Rest Labs main marketing tool is our Prescription that we leave with medical providers. Prescription is printed on 8.5 x 11 sheets of paper to create a prescription pad for our medical providers. Prescription should fit to one page. Quiet Harbor Rest Labs works with 250 different medical providers so it is important we are able to update and change the medical provider information at bottom. The medical provider would fill-out top with patient information, check-off center testing and patient co-morbidity and Fax to Quiet Harbor Rest Labs. Because it is Faxed to us it is important to have clear print and large font Attached or uploaded file is one example we currently use. Please review all 5 must haves.

Target Market(s)

Prescription for medical providers to fill-out and fax to Quiet Harbor Rest Labs to conduct the sleep study.

Industry/Entity Type

Medical

Colors

Designer to choose only greyscale colors for use in the design.

Requirements
Must have
• 1) Prescription Size: 8.5 x 11
• 2) Must fit to One page Only
• 3) Ability to change medical provider information at bottom of prescription. We work with 250 different medical providers
• 4) Ability to change or update any part of prescription
• 5) Document Must be created in Microsoft Word 2016. This is the program we use for our prescriptions.
Nice to have
• Can be done in Gray-Scale or Black and White since its being faxed from the medical provider to us.

```html
<!DOCTYPE html>
<html lang="en">
<head>
<meta charset="utf-8">
<title>Sleep Study Physician Order</title>
<link href="https://fonts.googleapis.com/css2?family=Roboto:ital,wght@0,300;0,400;0,500;0,700;1,400;1,700&family=Open+Sans:wght@600&display=swap" rel="stylesheet">
<style>
  :root{
    --ink:#111;
    --grey:#777;
    --grey-mid:#8a8a8a;
    --band:#d9d9d9;
    --rule:#555;
    --backdrop:#ececec;
    --paper:#fff;
  }
  *{box-sizing:border-box;margin:0;padding:0}
  html,body{width:1200px;height:1200px;overflow:hidden;background:var(--backdrop)}
  body{font-family:"Roboto",Arial,sans-serif;color:var(--ink)}
  .sheet{
    position:absolute;left:197px;top:30px;width:1240px;height:1755px;
    background:var(--paper);transform:scale(.65);transform-origin:top left;
  }
  .at{position:absolute;transform:translateY(-50%);white-space:nowrap}
  .brand{left:90px;top:132px;display:flex;align-items:center;gap:18px}
  .brand-mark{width:34px;height:34px;background:var(--grey)}
  .brand-name{font-size:34px;font-weight:700;line-height:1.15;color:var(--ink)}
  .title{left:400px;top:82px;font-size:56px;font-weight:700;letter-spacing:.3px}
  .contact{left:430px;top:143px;font-size:34px;font-weight:700;color:var(--grey);letter-spacing:-.5px}
  .address{left:485px;top:178px;font-size:22px;font-weight:700;color:var(--grey)}
  .field-row{left:96px;width:1044px;display:flex;align-items:flex-end;font-size:21px;font-weight:700}
  .blank{flex:1;border-bottom:1.5px solid var(--ink);height:20px;margin:0 4px}
  .band{position:absolute;background:var(--band);border:1.5px solid var(--rule);text-align:center;font-weight:700}
  .band-study{left:88px;top:418px;width:1068px;height:40px;font-size:28px;line-height:38px}
  .box{display:inline-block;width:16px;height:16px;border:2px solid var(--ink);box-shadow:2px 2px 0 var(--ink);vertical-align:middle;margin-right:14px}
  .box-lg{width:18px;height:18px}
  .study-main{left:93px;top:490px;font-size:36px;font-weight:500}
  .study-main em{font-size:28px;font-weight:300;color:#333}
  .study-sub{left:126px;font-size:36px;font-weight:500}
  .code{font-size:14px;font-weight:400}
  .study{left:90px;font-size:32px;font-weight:300}
  .note{left:132px;font-size:14px}
  .note i{font-style:italic}
  .heavy-rule{position:absolute;left:88px;top:920px;width:1076px;border-top:3px solid var(--ink)}
  .necessity{position:absolute;left:98px;top:935px;width:1066px;height:365px;border:1.5px solid var(--rule)}
  .necessity .band{left:-1.5px;top:-1.5px;width:1066px;height:36px;font-size:24px;line-height:34px}
  .conditions{position:absolute;top:46px;display:flex;flex-direction:column;font-size:23px;font-weight:700;letter-spacing:-.3px}
  .conditions li{list-style:none;display:flex;align-items:flex-start;line-height:32px}
  .conditions .box{margin-top:8px}
  .col-a{left:49px}
  .col-b{left:384px}.col-b li{line-height:34.5px}.col-b .box{margin-top:9px}
  .col-c{left:719px}.col-c li{line-height:34px}.col-c .box{margin-top:9px}
  .col-c .box{margin-right:22px}
  .other-line{display:inline-block;width:240px;border-bottom:1.5px solid var(--ink);height:24px}
  .clinic{left:0;width:1240px;top:1328px;text-align:center;font-family:"Open Sans",Arial,sans-serif;font-weight:600;font-size:36px}
  .clinic-line{left:170px;top:1373px;font-size:19px;font-weight:700}
  .clinic-line span{color:var(--grey);margin-right:20px}
  .provider{position:absolute;font-size:19px;font-weight:700}
  .provider .box{width:12px;height:12px;margin-right:12px}
  .npi{display:block;font-size:14px;color:var(--grey-mid);margin:8px 0 0 26px}
  .sign{left:107px;top:1543px;width:1063px;display:flex;align-items:flex-end;font-size:21px;font-weight:700}
  .date-blank{width:80px;border-bottom:1.5px solid var(--ink);height:20px}
  .fax-cta{left:0;width:1240px;top:1585px;text-align:center;font-size:29px;font-weight:700}
  .fax-cta span{color:var(--grey)}
  .attach{left:94px;top:1608px;width:1082px;height:35px;font-size:19px;line-height:33px;padding-left:30px;text-align:left;background:#f1f1f1}
  .attach .dot{color:var(--grey-mid)}
  .thanks{left:0;width:1240px;top:1673px;text-align:center;font-size:28px;font-weight:700;font-style:italic}
</style>
</head>
<body>
<main class="sheet">
  <div class="at brand"><span class="brand-mark"></span><span class="brand-name">Quiet Harbor<br>Rest Labs</span></div>
  <h1 class="at title">Sleep Study Physician Order</h1>
  <div class="at contact">Phone: (555) 210-4418 &nbsp;•&nbsp; Fax: (555) 210-4419</div>
  <div class="at address">820 Linden Crest Avenue, Suite 2-A; Fairview, NV 89014</div>

  <div class="at field-row" style="top:255px">Patient Name:<span class="blank"></span>DOB:<span class="blank" style="flex:0 0 95px"></span>/<span class="blank" style="flex:0 0 95px"></span>/<span class="blank" style="flex:0 0 95px"></span></div>
  <div class="at field-row" style="top:299px">Telephone:<span class="blank"></span>Alternate Telephone:<span class="blank" style="flex:0 0 305px"></span></div>
  <div class="at field-row" style="top:345px">Primary Insurance:<span class="blank"></span>Secondary Insurance:<span class="blank" style="flex:0 0 325px"></span></div>
  <div class="at field-row" style="top:391px">Height:<span class="blank"></span>Weight:<span class="blank"></span>Patient Gender (circle one): &nbsp;M &nbsp;/ &nbsp;F</div>

  <div class="band band-study">Diagnostic Sleep Study Ordered</div>

  <div class="at study-main"><span class="box box-lg"></span>Complete Sleep Study: <em>(Based on Insurance or Patient’s Choice)</em></div>
  <div class="at study-sub" style="top:532px">In Lab Sleep Study (PSG) or Home Sleep Study <span class="code">(PSG 95810 / HST 95806)</span></div>
  <div class="at study-sub" style="top:578px">with follow-up PAP Titration Study <span class="code">(PAP 95811 if positive for sleep apnea)</span></div>

  <div class="at study" style="top:635px"><span class="box box-lg"></span>PEDIATRIC SLEEP STUDY: PSG w/End Tidal CO2 Monitoring</div>
  <div class="at note" style="top:672px">(PSG 95782 under 6 years of age &amp; PSG 95810 older than 6 years of age)</div>
  <div class="at study" style="top:713px"><span class="box box-lg"></span>In-Lab Diagnostic Sleep Study/Polysomnogram</div>
  <div class="at study" style="top:763px"><span class="box box-lg"></span>SPLIT-NIGHT STUDY <span class="code">(PSG with PAP 95810 &amp; 95811) To Comply With Accreditation &amp; Insurance Guidelines:</span></div>
  <div class="at note" style="top:795px"><i>AHI must be 20 or greater with minimum 2 hour recorded sleep time and 3 hours minimum to complete PAP treatment</i></div>
  <div class="at study" style="top:845px"><span class="box box-lg"></span>CPAP / BiPAP / BiPAP ST Titration Study <span class="code">(Patients with documented sleep apnea 95811)</span></div>
  <div class="at study" style="top:895px"><span class="box box-lg"></span>Home Sleep Study <span class="code">(HST 95806 Conducted in patient’s home &amp; unattended by technologist) (No insurance patient cost $250.00)</span></div>
  <div class="heavy-rule"></div>

  <section class="necessity">
    <div class="band">Patient Medical Necessity – Please Check All Boxes That Apply</div>
    <ul class="conditions col-a">
      <li><span class="box"></span>Atrial Fibrillation</li>
      <li><span class="box"></span>Bipolar Disorder</li>
      <li><span class="box"></span>Congestive Heart Failure</li>
      <li><span class="box"></span>COPD</li>
      <li><span class="box"></span>Depression</li>
      <li style="line-height:28px"><span class="box" style="margin-top:6px"></span>Excessive Daytime<br>Sleepiness</li>
      <li><span class="box"></span>Gasping Sensations</li>
      <li><span class="box"></span>Frequent Awakenings</li>
      <li><span class="box"></span>Frequent Urination</li>
    </ul>
    <ul class="conditions col-b">
      <li><span class="box"></span>Heart Disease</li>
      <li><span class="box"></span>History Heart Attack</li>
      <li><span class="box"></span>Hypertension</li>
      <li><span class="box"></span>Insomnia</li>
      <li><span class="box"></span>Mental or Mood Disorder</li>
      <li><span class="box"></span>Loud Snoring</li>
      <li><span class="box"></span>Morbid Obesity / Obesity</li>
      <li><span class="box"></span>Morning Headaches</li>
      <li><span class="box"></span>Narcolepsy</li>
    </ul>
    <ul class="conditions col-c">
      <li><span class="box"></span>Opioid Use</li>
      <li><span class="box"></span>PTSD</li>
      <li><span class="box"></span>Pulmonary Disease</li>
      <li><span class="box"></span>Restless Leg Syndrome</li>
      <li><span class="box"></span>Seizures</li>
      <li><span class="box"></span>Shift Work Sleep disorder</li>
      <li><span class="box"></span>Stroke / TIA</li>
      <li><span class="box"></span>Witnessed Apnea</li>
      <li><span class="box"></span>Other<span class="other-line"></span></li>
    </ul>
  </section>

  <h2 class="at clinic">Silver Valley ENT Partners</h2>
  <div class="at clinic-line">4410 W. Meadow Lane; Fairview, NV 89016-2210 &nbsp;&nbsp;&nbsp;&nbsp;Telephone: <span>555-318-6620</span> Fax: <span>555-318-6621</span></div>

  <div class="provider" style="left:110px;top:1403px"><span class="box"></span>Dr. Adrian Cole Whitford<span class="npi">NPI: 1000000011</span></div>
  <div class="provider" style="left:475px;top:1403px"><span class="box"></span>Dr. Lena M. Hartwell<span class="npi">NPI: 1000000029</span></div>
  <div class="provider" style="left:832px;top:1403px"><span class="box"></span>Dr Marcus T. Delgrove<span class="npi">NPI: 1000000037</span></div>
  <div class="provider" style="left:110px;top:1462px"><span class="box"></span>Dr. Nora Vance<span class="npi">NPI: 1000000045</span></div>
  <div class="provider" style="left:475px;top:1462px"><span class="box"></span>Elise Brandt, FNP-C<span class="npi">NPI: 1000000052</span></div>
  <div class="provider" style="left:832px;top:1462px"><span class="box"></span>Owen Pryce, PA-C<span class="npi">NPI: 1000000060</span></div>

  <div class="at sign">Physician’s Signature:<span class="blank"></span>Date:&nbsp;<span class="date-blank"></span>/<span class="date-blank"></span>/<span class="date-blank"></span></div>
  <div class="at fax-cta">Please Fax: <span>555-210-4419</span> or Email: <span>quietharborrest@mail.example</span></div>
  <div class="band attach">☑&nbsp; Fax Along With: Patient Demographic Information <span class="dot">•</span> Copy of Current Insurance Information <span class="dot">•</span> Clinical Notes</div>
  <p class="at thanks">Thank You For your support JAMES &amp; ELLA</p>
</main>
</body>
</html>
```